RVM Photography Business Card Design

I would like a business card designed in the shape of a camera.
Would like to see various camera designs. Would like to see what the card looks like in different colors. Would like to see which logo looks better on the various camera designs so please show me some with the white logo and some with the black logo. If you need a different file formats please let me know.
Project Deadline Extended Reason: My grandfather passed away and dealing with funeral plans so need to extend deadline. Added Tuesday, March 1, 2016
Project Deadline Extended
Reason: I just got back from out of town. My grandfather's passing was the primary focus for me these past few weeks and the funeral is over so now I will concentrate on picking my business card design. I really appreciate each designer who has taken the time to submit a design. Your effort has not gone unnoticed. I look forward to seeing more amazing designs.
Industry/Entity Type
Business
Contact Information for Business Card
Corinne
757-418-2296
https://www.facebook.com/rvmphotographyfreelance/
NoraCorinne@rvm-studiowork.example

```html
<!DOCTYPE html>
<html lang="en">
<head>
<meta charset="utf-8">
<title>RVM Photography – Business Card</title>
<link href="https://fonts.googleapis.com/css2?family=Cinzel:wght@400;500&family=Open+Sans:wght@400;700&display=swap" rel="stylesheet">
<style>
  :root {
    --backdrop: #e4e4e4;
    --gold-dark: #8a6a1f;
    --gold-mid: #c9a44a;
    --gold-light: #ecd186;
    --body-black: #050505;
    --ring-white: #ffffff;
  }
  html, body {
    margin: 0;
    padding: 0;
    width: 1200px;
    height: 800px;
    overflow: hidden;
    background: var(--backdrop);
  }
  .stage {
    width: 1200px;
    height: 800px;
    display: flex;
    align-items: center;
    justify-content: center;
  }
  .business-card {
    width: 900px;
    height: 514px;
    display: block;
    box-shadow: 0 20px 40px rgba(0,0,0,0.18);
  }
  .studio-title {
    font-family: "Cinzel", serif;
    font-size: 42px;
    font-weight: 400;
    letter-spacing: 1px;
  }
  .logo-name {
    font-family: "Cinzel", serif;
    font-size: 58px;
    font-weight: 500;
  }
  .contact {
    font-family: "Open Sans", sans-serif;
    font-size: 20px;
  }
  .contact-name {
    font-weight: 700;
  }
</style>
</head>
<body>
<main class="stage">
  <svg class="business-card" viewBox="0 0 900 514" xmlns="http://www.w3.org/2000/svg" aria-label="RVM Photography business card shaped like a camera">
    <defs>
      <linearGradient id="goldBrushed" x1="0" y1="0" x2="1" y2="0.3">
        <stop offset="0" style="stop-color: var(--gold-dark)"/>
        <stop offset="0.35" style="stop-color: var(--gold-light)"/>
        <stop offset="0.65" style="stop-color: var(--gold-mid)"/>
        <stop offset="1" style="stop-color: var(--gold-dark)"/>
      </linearGradient>
      <radialGradient id="goldDisc" cx="0.4" cy="0.35" r="0.75">
        <stop offset="0" style="stop-color: var(--gold-light)"/>
        <stop offset="0.6" style="stop-color: var(--gold-mid)"/>
        <stop offset="1" style="stop-color: var(--gold-dark)"/>
      </radialGradient>
    </defs>

    <rect class="card-base" x="0" y="0" width="900" height="514" fill="url(#goldBrushed)"/>

    <g class="camera-body" fill="var(--body-black)">
      <path class="viewfinder" d="M250 104 L300 44 L540 44 L590 104 Z"/>
      <rect class="shutter-slot" x="80" y="80" width="170" height="20" rx="10"/>
      <rect class="dial-slot" x="640" y="36" width="140" height="28" rx="14"/>
      <rect class="body-shell" x="0" y="100" width="900" height="392" rx="70"/>
    </g>

    <rect class="trim-line" x="0" y="212" width="900" height="6" fill="url(#goldBrushed)"/>

    <text class="studio-title" x="420" y="150" text-anchor="middle" fill="url(#goldBrushed)">RVM PHOTOGRAPHY</text>

    <g class="lens-logo">
      <circle cx="600" cy="292" r="108" fill="url(#goldDisc)" stroke="var(--ring-white)" stroke-width="24"/>
      <text class="logo-name" x="600" y="313" text-anchor="middle" fill="var(--body-black)">RVM</text>
    </g>

    <g class="contact" fill="var(--gold-light)">
      <text class="contact-name" x="22" y="398">CORINNE</text>
      <text x="22" y="424">(757) 418-2296</text>
      <text x="22" y="450">facebook.com/rvmphotographyfreelance/</text>
      <text x="22" y="476">NoraCorinne@rvm-studiowork.example</text>
    </g>
  </svg>
</main>
</body>
</html>
```